Modernes Karten-Design für Finanzdienstleister
Zielgruppe
Wir sind ein Finanzdienstleister, der zum einen Teil auf Provisionsbasis und zum anderen Teil auf Honorarbasis arbeitet. Hierfür haben wir auch getrennte Firmenbereiche. Unser Kundenklientel sind Privatpersonen im Alter zwischen 35 und 80 Jahren. Unsere Dienstleistungen drehen sich um alle Versicherungen, aber auch um Geldanlagen, Verfügungen, Vollmachten und Testamente
Aufgabenstellung
Wir benötigen eine Karte, die wir an Kunden verschicken, wenn wir Unterlagen verschicken. Die Karte, die wir bisher haben finden Sie bei den Dateien, die wir hochgeladen haben. Wir möchten nun eine moderne Karte haben mit der wir uns bei unseren Kunden bedanken. Auf der Rückseite der Karte soll wie bisher Platz sein für einen handschriftlichen Gruß von uns oder für sonstige handschriftliche Vermerke. Beim Format der Karte sind wir fexibel. Es müssen unsere Firmenfarben und unser Slogan verwendet werden. Wir möchten ein schnörkelloses modernes Design haben. Bei den hochgeladenen Unterlagen befinden sich auch Vorschläge, die ein Mitarbeiter bereits entworfen hat. Diese gefallen uns aber nicht. Die Webadresse unserer Webseite lautet: https://lindmayr-horizonte.de/
Auf der Rückseite sollen natürlich auch die Adress- und Kontaktdaten mit drauf sein. Wir brauchen hier keine eigenen Bilder und auch kein Stockmaterial. Die Karte soll einfach, schlicht aber stylisch modern sein.

```html
<!DOCTYPE html>
<html lang="de">
<head>
<meta charset="utf-8">
<title>Dankeskarte – lindmayr horizonte</title>
<link rel="stylesheet" href="https://fonts.googleapis.com/css2?family=Montserrat:wght@800&family=Fira+Sans:wght@500&family=Arimo:wght@400&display=swap">
<style>
  :root {
    --stage: #cbcbcb;
    --orange: #ec6d00;
    --orange-deep: #e8590c;
    --white: #ffffff;
    --ink: #111111;
  }
  * { margin: 0; padding: 0; box-sizing: border-box; }
  html, body {
    width: 1200px; height: 1200px; overflow: hidden;
    background: var(--stage);
  }
  .card {
    position: absolute;
    left: 230px;
    width: 748px;
    height: 530px;
    box-shadow: 1px 2px 4px rgba(0,0,0,0.35);
  }
  .card--front { top: 48px; background: var(--orange); overflow: hidden; }
  .card--back { top: 625px; background: var(--white); }

  .front-pattern {
    position: absolute; inset: 0;
    background: linear-gradient(135deg, var(--orange) 0%, var(--orange-deep) 100%);
    opacity: 0.9;
  }
  .front-title {
    position: absolute;
    left: 0; right: 0;
    top: 168px;
    text-align: center;
    padding-left: 10px;
    font-family: "Montserrat", sans-serif;
    font-weight: 800;
    font-size: 180px;
    line-height: 1;
    letter-spacing: -2px;
    color: var(--white);
  }

  .brand {
    position: absolute;
    left: 38px; top: 36px;
    font-family: "Fira Sans", sans-serif;
    font-weight: 500;
    font-size: 37px;
    line-height: 1;
    color: var(--ink);
    letter-spacing: -0.3px;
  }
  .slogan {
    position: absolute;
    left: 38px; width: 314px; top: 82px;
    text-align: center;
    font-family: "Fira Sans", sans-serif;
    font-weight: 500;
    font-size: 18px;
    color: var(--ink);
    letter-spacing: 0.3px;
  }

  .contact {
    position: absolute;
    left: 404px; top: 45px;
    font-family: "Arimo", sans-serif;
    font-style: normal;
    font-size: 11.5px;
    line-height: 13px;
    color: var(--ink);
    letter-spacing: -0.2px;
  }
  .contact .sep {
    display: inline-block;
    width: 4px; height: 4px;
    background: var(--orange);
    margin: 0 3px 2px;
    vertical-align: middle;
  }
  .contact-rule {
    position: absolute;
    left: 404px; right: 0; top: 77px;
    height: 1.5px;
    background: var(--orange);
  }
</style>
</head>
<body>
  <section class="card card--front">
    <div class="front-pattern" role="img" aria-label="Wiederholtes Muster aus den Buchstaben D A N K E und kleinen Herzen in dunklerem Orange"></div>
    <h1 class="front-title">DANKE</h1>
  </section>

  <section class="card card--back">
    <div class="brand">lindmayr horizonte</div>
    <p class="slogan">Weiter nach vorn denken.</p>
    <address class="contact">
      Birkenweg 12<span class="sep"></span>79098 Freiburg<span class="sep"></span>Tel. 0761 482739-14<br>
      info@lindmayr-horizonte.de<span class="sep"></span>www.lindmayr-horizonte.de
    </address>
    <div class="contact-rule"></div>
  </section>
</body>
</html>
```